Corvena Card

The logo is the Spanish flag colors I want a vibrant eye catching design with the yellow / red colors over either Navy or white background or black even ,
Would like a 2D feel to the logo with another lighter color logo under it look ,

Contact Information for Business Card

Corvena Flooring
Tobin Reswick
Main Number
Cell Number
Fax Number

Website on the side of the card somewhere

Font styles to use
Sans Serif

Colors
ec1f27
ffc214

Requirements
Must have
• 2 logos feel one is bolder and the other one underneath very light

```html
<!DOCTYPE html>
<html lang="en">
<head>
<meta charset="utf-8">
<title>Corvena Flooring – Business Card</title>
<link href="https://fonts.googleapis.com/css2?family=Arimo:wght@400;700&family=Michroma&display=swap" rel="stylesheet">
<style>
  :root {
    --page-bg: #ececec;
    --card-white: #f7f7f7;
    --card-navy: #121846;
    --brand-red: #ec1f27;
    --brand-gold: #e5b02c;
    --text-grey: #6b6b6b;
    --divider: #9a9a9a;
    --silver: #d9dbe0;
  }
  * { margin: 0; padding: 0; box-sizing: border-box; }
  html, body { width: 1200px; height: 801px; overflow: hidden; }
  body {
    background: var(--page-bg);
    font-family: "Arimo", Arial, sans-serif;
    position: relative;
  }
  .card {
    position: absolute;
    top: 252px;
    width: 520px;
    height: 297px;
    box-shadow: 0 6px 18px rgba(0,0,0,0.18);
  }
  .card--front { left: 50px; background: var(--card-white); }
  .card--back { left: 630px; background: var(--card-navy); }

  .brand {
    position: absolute;
    left: 0; right: 0;
    display: flex;
    flex-direction: column;
    align-items: center;
    font-family: "Michroma", sans-serif;
  }
  .brand__mark {
    width: 44px; height: 44px;
    margin-bottom: 12px;
  }
  .brand__name {
    font-size: 25px;
    letter-spacing: 5px;
    line-height: 1;
  }
  .brand__sub {
    font-size: 11px;
    letter-spacing: 7px;
    margin-top: 6px;
  }
  .card--front .brand { top: 26px; color: var(--brand-gold); }
  .card--front .brand__mark { background: var(--brand-red); }
  .card--back .brand { top: 88px; color: var(--silver); }
  .card--back .brand__mark { background: var(--silver); }

  .identity {
    position: absolute;
    left: 40px; top: 164px;
    width: 190px;
    text-align: right;
  }
  .identity__name {
    color: var(--brand-red);
    font-weight: 700;
    font-size: 21px;
  }
  .identity__role {
    color: var(--text-grey);
    font-size: 15px;
    margin-top: 4px;
  }
  .divider {
    position: absolute;
    left: 248px; top: 160px;
    width: 1px; height: 64px;
    background: var(--divider);
  }
  .contacts {
    position: absolute;
    left: 264px; top: 158px;
    list-style: none;
  }
  .contacts li {
    display: flex;
    align-items: center;
    gap: 8px;
    color: var(--text-grey);
    font-size: 14px;
    height: 22px;
  }
  .contacts svg { width: 14px; height: 14px; flex: none; }
  .accent { color: var(--brand-red); }
  .address {
    position: absolute;
    left: 0; right: 0; bottom: 28px;
    text-align: center;
    color: var(--text-grey);
    font-size: 14px;
  }
</style>
</head>
<body>
  <section class="card card--front">
    <div class="brand">
      <span class="brand__mark"></span>
      <span class="brand__name">CORVENA</span>
      <span class="brand__sub">FLOORING</span>
    </div>

    <div class="identity">
      <p class="identity__name">Dara Whitlow</p>
      <p class="identity__role">Manager</p>
    </div>
    <span class="divider"></span>

    <ul class="contacts">
      <li>
        <svg viewBox="0 0 16 16" aria-hidden="true"><circle cx="8" cy="8" r="8" fill="#ec1f27"/><path d="M5 4.5c.6-.5 1.2 0 1.5.8l.3.8c.1.4-.2.7-.5 1 .4.9 1 1.6 1.9 2 .3-.3.6-.6 1-.5l.8.3c.8.3 1.2.9.7 1.5-1 1.2-3 .4-4.4-1S3.8 5.5 5 4.5z" fill="#fff"/></svg>
        555-208-7413
      </li>
      <li>
        <svg viewBox="0 0 16 16" aria-hidden="true"><rect x="1" y="3" width="14" height="10" fill="#ec1f27"/><path d="M1 3l7 6 7-6" fill="none" stroke="#fff" stroke-width="1.3"/></svg>
        youremail@mailbox.com
      </li>
      <li>
        <svg viewBox="0 0 16 16" aria-hidden="true"><circle cx="8" cy="8" r="7.5" fill="#ec1f27"/><g fill="none" stroke="#fff" stroke-width="1"><circle cx="8" cy="8" r="5"/><ellipse cx="8" cy="8" rx="2.2" ry="5"/><path d="M3 8h10"/></g></svg>
        <span>www.<span class="accent">yourwebsite</span>.com</span>
      </li>
    </ul>

    <p class="address">Your address, city, state, ZIP 0000</p>
  </section>

  <section class="card card--back">
    <div class="brand">
      <span class="brand__mark"></span>
      <span class="brand__name">CORVENA</span>
      <span class="brand__sub">FLOORING</span>
    </div>
  </section>
</body>
</html>
```